Business Card - high end, modern health care

Hey designers!

We need a double sided business card for the boutique, cutting edge physical therapy rehabilitation centre in Sydney's Northern Beaches.

With the most qualified physios in the area The Harbourline Motion Clinic does what other physiotherapy practices do not, we take our time with our patients giving them longer appointments, better physios and therefor faster results!

We guarantee that the service people receive at THMC will be unparalleled.

Hence we need a business card to reflect our modern, boutique, high end service. The final design needs to reflect that we are in a class of our own yet with the feel of beachside retreat.

Below I have attached our logo in both blue on white and white on blue. The exact colour is;
and the font that we have used in our logo is Tex Gyre Aventador.

I like the idea of the blue as the main colour as it is more eye catching and our signage onto the main road will be in this blue and in the interest of consistency across marketing the blue needs to be a part of the design. However I would appreciate a few designs onto a wooden background as this is a visual theme within the fitout of the practice.

The design needs to be of standard size (91x55mm).

Target Market(s)

We target people who have an end outcome in mind and those who have had poor experiences with other providers and ensure that everyone gets the care that they deserve with a premium service that is tailored to the individuals circumstances. As a premium service, the target market is highly educated, business and tech savvy with the additional target market of elderly people who have self funded their retirement and see value in paying for the best ongoing rehabilitation to maintain independence.

Industry/Entity Type

Physical Therapy

Contact Information for Business Card

Name, designation( Titled Musculoskeletal Physiotherapist... there will also be those in the company that have multiple designations ie 5 or 6 words long), phone number, email, facebook, instagram, address

Font styles to use
Sans Serif

Colors

Designer to choose colors to be used in the design.

Requirements
Must have
• Front - The logo as large as possible, blue or wooden theme, and all of the important details.
• Back - A blank space/lines on which to write appointment times (no "Appointment, date, time" etc.)
Nice to have
• facebook url
• logos for facebook and instagram
• Mini logos for the phone and email?

```html
<!DOCTYPE html>
<html lang="en">
<head>
<meta charset="utf-8">
<title>The Harbourline Motion Clinic – Business Card</title>
<link rel="stylesheet" href="https://fonts.googleapis.com/css2?family=Roboto:wght@400;500;700&family=Roboto+Condensed:wght@700&display=swap">
<style>
  :root {
    --brand-blue: #0b57a8;
    --ink-grey: #555a60;
    --rule-grey: #6b6f74;
    --card-front: #f1f1f1;
    --card-back: #ffffff;
    --watermark: #f0f3f8;
    --backdrop: #2b2b2b;
  }
  * { margin: 0; padding: 0; box-sizing: border-box; }
  html, body { width: 1200px; height: 960px; overflow: hidden; }
  body {
    background: var(--backdrop);
    position: relative;
    font-family: "Roboto", Arial, sans-serif;
  }
  .card {
    position: absolute;
    width: 600px;
    height: 342px;
    border-radius: 16px;
    overflow: hidden;
  }
  .card--front { left: 322px; top: 108px; background: var(--card-front); }
  .card--back { left: 320px; top: 493px; background: var(--card-back); }

  /* Front */
  .holder { position: absolute; left: 27px; top: 28px; }
  .holder__name {
    font-family: "Roboto Condensed", Arial, sans-serif;
    font-weight: 700; font-size: 21px; color: var(--brand-blue); line-height: 24px;
  }
  .holder__title { font-size: 14.5px; font-weight: 500; color: var(--ink-grey); line-height: 20px; }
  .address {
    position: absolute; left: 27px; top: 110px;
    font-size: 14.5px; font-style: normal; color: var(--ink-grey); line-height: 18px;
  }
  .contacts {
    position: absolute; left: 27px; top: 156px; list-style: none;
    font-size: 14.5px; color: var(--ink-grey);
  }
  .contacts li { display: flex; align-items: center; height: 19.2px; }
  .contacts svg { width: 14px; height: 14px; margin-right: 9px; fill: var(--brand-blue); flex: none; }
  .clinic-name {
    position: absolute; left: 27px; top: 268px;
    font-weight: 700; font-size: 21px; line-height: 23px; letter-spacing: 0.3px;
    color: var(--brand-blue); text-transform: uppercase;
  }
  .brand-disc {
    position: absolute; left: 255px; top: 4px;
    width: 336px; height: 336px; border-radius: 50%;
    background: var(--brand-blue);
  }

  /* Back */
  .watermark-disc {
    position: absolute; left: 150px; top: 28px;
    width: 300px; height: 300px; border-radius: 50%;
    background: var(--watermark);
  }
  .appointment-form { position: absolute; left: 32px; top: 40px; width: 527px; color: var(--ink-grey); font-size: 16px; }
  .field { display: flex; align-items: flex-end; height: 22px; }
  .field__rule { flex: 1; border-bottom: 1px solid var(--rule-grey); margin: 0 4px 5px 2px; }
  .field--name { margin-bottom: 21px; }
  .field__rule--time { flex: 0 0 115px; }
  .blank-line { height: 40px; border-bottom: 1px solid var(--rule-grey); margin-left: 3px; }
  .blank-line--first { height: 34px; }
</style>
</head>
<body>

<section class="card card--front" aria-label="Card front">
  <div class="brand-disc" aria-hidden="true"></div>

  <div class="holder">
    <p class="holder__name">LIAM HARCOURT</p>
    <p class="holder__title">CEO/FOUNDER</p>
  </div>

  <address class="address">
    14 Pittwater Road<br>Collaroy, NSW 2097
  </address>

  <ul class="contacts">
    <li><svg viewBox="0 0 24 24"><path d="M6.6 10.8a15 15 0 006.6 6.6l2.2-2.2c.3-.3.7-.4 1-.2 1.1.4 2.3.6 3.6.6.6 0 1 .4 1 1V20c0 .6-.4 1-1 1A17 17 0 013 4c0-.6.4-1 1-1h3.5c.6 0 1 .4 1 1 0 1.3.2 2.5.6 3.6.1.3 0 .7-.2 1z"/></svg>02 9555 0147</li>
    <li><svg viewBox="0 0 24 24"><path d="M2 5h20v14H2z M3.5 6.5l8.5 6 8.5-6" fill="none" stroke="#0b57a8" stroke-width="2.4"/><path d="M2 5h20v3l-10 6L2 8z"/></svg>liam@harbourline.com</li>
    <li><svg viewBox="0 0 24 24"><circle cx="12" cy="12" r="9.5" fill="none" stroke="#0b57a8" stroke-width="2.5"/><path d="M2.5 12h19M12 2.5c3 3 3 16 0 19M12 2.5c-3 3-3 16 0 19" fill="none" stroke="#0b57a8" stroke-width="2"/></svg>www.harbourline.com</li>
    <li><svg viewBox="0 0 24 24"><rect x="3" y="3" width="18" height="18" rx="2"/></svg>/harbourlineclinic</li>
    <li><svg viewBox="0 0 24 24"><rect x="3" y="3" width="18" height="18" rx="2"/></svg>@harbourline</li>
  </ul>

  <p class="clinic-name">The Harbourline<br>Motion Clinic</p>
</section>

<section class="card card--back" aria-label="Card back">
  <div class="watermark-disc" aria-hidden="true"></div>
  <div class="appointment-form">
    <div class="field field--name">Name<span class="field__rule"></span></div>
    <div class="field field--date">Date<span class="field__rule"></span>Time<span class="field__rule field__rule--time"></span>&nbsp;am/pm</div>
    <div class="blank-line blank-line--first"></div>
    <div class="blank-line"></div>
    <div class="blank-line"></div>
    <div class="blank-line"></div>
    <div class="blank-line"></div>
  </div>
</section>

</body>
</html>
```